Letterhead

We would like to use the logo attached as a new letterhead. Our problem is that we think the dark blue background is too much. We'd like a sleek, professional letterhead, and we'd like at least five options to choose from. I've also uploaded our old letterhead for reference of the style we're going for.

```html
<!DOCTYPE html>
<html lang="en">
<head>
<meta charset="utf-8">
<title>Stationery Set Design 7</title>
<link rel="stylesheet" href="https://fonts.googleapis.com/css2?family=Jost:wght@400;600&family=PT+Sans:wght@700&display=swap">
<style>
  :root {
    --board: #dcdddf;
    --board-gold: #c8b790;
    --navy: #1c2f4e;
    --gold: #c6a462;
    --gold-text: #c19a55;
    --heading: #58595b;
    --paper: #ffffff;
  }
  * { box-sizing: border-box; margin: 0; padding: 0; }
  html, body { width: 1200px; height: 951px; overflow: hidden; }
  body {
    position: relative;
    background: var(--board);
    font-family: "Jost", "Century Gothic", sans-serif;
    color: var(--navy);
  }
  .board-accent { position: absolute; inset: 0; }
  .sheet-title {
    position: absolute;
    font-family: "PT Sans", "Myriad Pro", sans-serif;
    font-weight: 700;
    font-size: 22px;
    color: var(--heading);
    line-height: 1;
  }
  .paper {
    position: absolute;
    background: var(--paper);
    box-shadow: 0 3px 14px rgba(0,0,0,.28);
    overflow: hidden;
  }
  .brand-block {
    position: absolute;
    width: 126px; height: 66px;
    background: var(--navy);
    display: flex; flex-direction: column; justify-content: center;
    padding-left: 14px;
    color: #ffffff;
    font-weight: 400;
    font-size: 12.5px;
    letter-spacing: .12em;
    line-height: 1.25;
  }
  .rule-h, .rule-v { position: absolute; background: var(--gold); }
  .rule-h { height: 1px; right: 0; }
  .rule-v { width: 1px; }

  /* Letterhead */
  .letterhead { left: 55px; top: 185px; width: 483px; height: 624px; }
  .letterhead .brand-block { left: 11px; top: 1px; }
  .letterhead .rule-h { left: 137px; }
  .letterhead .rule-v { top: 67px; bottom: 0; }
  .sender {
    position: absolute; right: 18px; top: 35px; text-align: right;
  }
  .sender-name { font-size: 12px; letter-spacing: .04em; line-height: 1.2; }
  .sender-role { font-size: 9px; color: var(--gold-text); letter-spacing: .05em; margin-top: 2px; }
  .contact-line {
    position: absolute; right: 18px; top: 597px;
    font-size: 9.2px; font-weight: 600; white-space: nowrap;
  }
  .contact-line .sep { color: var(--gold); padding: 0 3px; font-weight: 400; }

  /* Envelope front */
  .envelope-front { left: 607px; top: 199px; width: 538px; height: 234px; }
  .envelope-front .brand-block { left: 8px; top: 0; }
  .envelope-front .rule-h { left: 134px; }
  .envelope-front .rule-v { top: 66px; bottom: 0; }
  .return-address {
    position: absolute; left: 146px; top: 40px;
    font-size: 9.2px; letter-spacing: .06em; white-space: nowrap;
  }

  /* Envelope back */
  .envelope-back { left: 607px; top: 525px; width: 538px; height: 233px; }
  .flap {
    position: absolute; left: 0; top: 0; width: 100%; height: 76px;
    border-radius: 0 0 24px 24px;
    background: linear-gradient(90deg, #8b7748 0%, #a78f5a 30%, #c4a462 50%, #a78f5a 72%, #8b7748 100%);
  }
  .flap-mark {
    position: absolute; left: 263px; top: 38px; width: 12px; height: 12px;
    background: #ffffff;
  }
</style>
</head>
<body>
  <svg class="board-accent" width="1200" height="951" viewBox="0 0 1200 951" aria-hidden="true">
    <polygon points="1200,6 1200,951 467,951" fill="var(--board-gold)"/>
  </svg>

  <h2 class="sheet-title" style="left:56px; top:148px;">Letterhead Design_7</h2>
  <h2 class="sheet-title" style="left:608px; top:158px;">Envelope Front Design_7</h2>
  <h2 class="sheet-title" style="left:608px; top:485px;">Envelope Back Design_7</h2>

  <section class="paper letterhead">
    <div class="brand-block"><span>CIVIC HALL</span><span>STRATEGIES</span></div>
    <div class="rule-h" style="top:16px;"></div>
    <div class="rule-h" style="top:25px;"></div>
    <div class="rule-h" style="top:33px;"></div>
    <div class="rule-v" style="left:24px;"></div>
    <div class="rule-v" style="left:32px;"></div>
    <div class="rule-v" style="left:40px;"></div>
    <div class="sender">
      <p class="sender-name">Marcus L. Arden, PC</p>
      <p class="sender-role">Governmental Affairs Consulting, Attorney at Law</p>
    </div>
    <p class="contact-line">907 555 0148<span class="sep">|</span>marcus@ardenlaw.com<span class="sep">|</span>318 K Street, Suite 210, Juneau, Alaska 99801</p>
  </section>

  <section class="paper envelope-front">
    <div class="brand-block"><span>CIVIC HALL</span><span>STRATEGIES</span></div>
    <div class="rule-h" style="top:16px;"></div>
    <div class="rule-h" style="top:24px;"></div>
    <div class="rule-h" style="top:33px;"></div>
    <div class="rule-v" style="left:22px;"></div>
    <div class="rule-v" style="left:30px;"></div>
    <div class="rule-v" style="left:38px;"></div>
    <p class="return-address">318 K Street, Suite 210, Juneau, Alaska 99801</p>
  </section>

  <section class="paper envelope-back">
    <div class="flap"><span class="flap-mark"></span></div>
  </section>
</body>
</html>
```